Halvern Dental website redesign

We need a redesign for a website: myhalverndental.com.

I already created a video going over what exactly is needed in the design.

See Video here: https://files.quorvane.com/file/d/8xKpQ2mWn4TzLrV7bHsYcE3jFuGaD6oN1/view?usp=sharing

Google Slide shown in Video: https://slides.quorvane.com/presentation/d/7RtW2yQnXbVc4LmPz9KsHdJf3GaE8oUi6TeYqNvB5wZx/edit?usp=sharing
Updates

Holidays in India so we did not get enough design entries or quality.

Target Market(s)

Dentistry

Industry/Entity Type

Dentistry

Number of Pages Required

1 page

Colors
0094D4
00A9DD
6FCCEA
C7EBF8
E9F6FB
00AB8E
00BBA5
67D7C9
C6EFE9
E9F9F6

Requirements
Must have
• See 13 min video link in description - shows what to do.

```html
<!DOCTYPE html>
<html lang="en">
<head>
<meta charset="utf-8">
<title>Halvern Dental</title>
<link rel="stylesheet" href="https://fonts.googleapis.com/css2?family=Gilda+Display&family=Poppins:wght@300;400;500;600;700&display=swap">
<style>
:root{
  --green:#69b12e;
  --green-dark:#5a9c25;
  --blue:#2d9be6;
  --blue-soft:#4aa9ea;
  --ink:#333c40;
  --muted:#5d666a;
  --night:#15242b;
  --gray-bg:#eef1f3;
  --white:#ffffff;
  --star:#f5c518;
}
*{margin:0;padding:0;box-sizing:border-box}
html,body{width:1200px;height:4082px;overflow:hidden}
body{position:relative;background:var(--white);font-family:"Poppins",sans-serif;color:var(--ink)}
.abs{position:absolute}
.serif{font-family:"Gilda Display",serif;font-weight:400}
.btn{position:absolute;display:flex;align-items:center;justify-content:center;border-radius:20px;color:var(--white);font-family:"Gilda Display",serif;font-size:17px;text-decoration:none}
.btn-green{background:var(--green)}
.btn-blue{background:var(--blue)}

/* header */
.site-header{position:absolute;left:0;top:0;width:1200px;height:97px;background:var(--white)}
.brand{position:absolute;left:60px;top:22px;font-family:"Gilda Display",serif;font-size:26px;color:var(--green)}
.brand-phone{position:absolute;left:68px;top:66px;font-size:14px;font-weight:600;color:var(--ink)}
.main-nav{position:absolute;left:440px;top:64px;display:flex;gap:0;font-size:11.5px;color:var(--ink)}
.main-nav span{padding:0 11px 6px}
.main-nav .active{color:var(--green);border-bottom:2px solid var(--green)}

/* hero */
.hero-photo{position:absolute;left:0;top:97px;width:1200px;height:637px;background:linear-gradient(110deg,#1f5f9c 0%,#2a84d6 45%,#3c9ee8 100%)}
.hero-title{position:absolute;left:60px;top:238px;font-size:57px;line-height:60px;font-weight:600;color:var(--white)}
.hero-sub{position:absolute;left:60px;top:368px;font-size:15.5px;color:var(--white)}
.social-dot{position:absolute;width:32px;height:32px;border:1.5px solid var(--white);border-radius:50%}
.slider-btn{position:absolute;width:38px;height:38px;border-radius:50%;display:flex;align-items:center;justify-content:center}

/* experience */
.section-title{position:absolute;width:1200px;left:0;text-align:center;font-family:"Gilda Display",serif;color:var(--green)}
.rule{position:absolute;height:3px;background:var(--blue)}
.about-text{position:absolute;left:596px;top:893px;width:468px;font-size:11.6px;line-height:21px;color:var(--muted)}
.about-text p{margin-bottom:10px}
.about-link{position:absolute;left:596px;top:1250px;font-family:"Gilda Display",serif;font-size:16px;color:var(--green);text-decoration:underline}

/* team */
.team-bg{position:absolute;left:0;top:1340px;width:1200px;height:1188px;background:var(--gray-bg)}
.team-intro{position:absolute;left:340px;top:1478px;width:520px;text-align:center;font-size:11.5px;line-height:20px;color:var(--ink)}
.team-card{position:absolute;top:1653px;width:262px;height:189px;background:var(--white);border-radius:4px;text-align:center}
.team-photo{position:absolute;top:-76px;left:55px;width:152px;height:152px;border-radius:50%;border:4px solid var(--green);background:radial-gradient(circle at 50% 45%,#b88a6a 0%,#5a4438 55%,#3a3432 100%)}
.team-name{position:absolute;top:112px;width:100%;font-family:"Gilda Display",serif;font-size:18px;color:var(--blue)}
.team-role{position:absolute;top:141px;width:100%;font-size:11px;color:var(--green)}

/* services */
.services-title{position:absolute;left:111px;top:2055px;font-family:"Gilda Display",serif;font-size:34px;color:var(--green)}
.services-intro{position:absolute;left:111px;top:2130px;width:420px;font-size:11.5px;line-height:20px;color:var(--white)}
.service{position:absolute;width:170px;text-align:center}
.service-icon{width:60px;height:60px;margin:0 auto;border-radius:3px;background:var(--white);display:flex;align-items:center;justify-content:center}
.service-icon.is-active{background:var(--green)}
.service-label{margin-top:12px;font-family:"Gilda Display",serif;font-size:16px;color:var(--white)}

/* insurance band */
.insurance{position:absolute;left:0;top:2528px;width:1200px;height:124px;background:var(--green)}
.insurance h3{position:absolute;left:276px;top:36px;font-family:"Gilda Display",serif;font-weight:400;font-size:27px;color:var(--white)}
.insurance p{position:absolute;left:276px;top:73px;font-size:11.5px;color:var(--white)}

/* reviews */
.review-card{position:absolute;left:277px;top:2945px;width:645px;height:239px;border:1.5px solid #e3e7ea;border-radius:16px;background:var(--white)}
.review-text{position:absolute;left:141px;top:60px;width:465px;font-size:11.4px;line-height:19.5px;color:var(--muted)}
.review-name{position:absolute;left:140px;top:180px;font-family:"Gilda Display",serif;font-size:18px;color:var(--green)}
.review-source{position:absolute;left:513px;top:176px;font-size:24px;font-weight:700;color:#222}
.arrow{position:absolute;font-size:40px;font-weight:300;color:var(--blue)}

/* promo */
.promo-photo{position:absolute;left:0;top:3313px;width:1200px;height:600px;background:linear-gradient(100deg,#1d74c2 0%,#2e95e4 55%,#4fb0ef 100%)}
.promo-person{position:absolute;left:71px;top:3241px;width:476px;height:500px;border-radius:44% 44% 8px 8px;background:linear-gradient(180deg,#e8c89a 0%,#f1e1cf 40%,#f7f7f7 100%)}
.promo-title{position:absolute;left:637px;top:3372px;font-family:"Gilda Display",serif;font-size:33px;line-height:41px;color:var(--white)}
.promo-sub{position:absolute;left:640px;top:3486px;font-size:11.5px;color:var(--white)}

/* footer */
.footer-head{position:absolute;top:3780px;font-family:"Gilda Display",serif;font-size:16px;color:var(--green)}
.footer-line{position:absolute;font-size:11.5px;color:var(--white);line-height:19px}
.footer-brand{position:absolute;left:76px;top:3884px;font-family:"Gilda Display",serif;font-size:30px;color:var(--green)}
.map{position:absolute;left:886px;top:3829px;width:250px;height:116px;background:linear-gradient(135deg,#e9ecef,#d7dde2)}
.copyright{position:absolute;left:0;top:4034px;width:1200px;height:48px;background:var(--green);color:var(--white);font-size:11px;text-align:center;line-height:48px}
</style>
</head>
<body>

<!-- Header -->
<header class="site-header">
  <div class="brand">Halvern Dental</div>
  <div class="brand-phone">(714) 555-0182</div>
  <a class="btn btn-green" style="left:840px;top:10px;width:158px;height:36px;font-size:15px">Schedule Online</a>
  <a class="btn btn-blue" style="left:1005px;top:10px;width:136px;height:36px;font-size:15px">Emergency</a>
  <nav class="main-nav">
    <span class="active">Home</span><span>About Us</span><span>Services ▾</span><span>Financing</span><span>Testimonials</span><span>New Patient Visit</span><span>Specials ▾</span><span>Contact Us</span><span>Blog</span>
  </nav>
</header>

<!-- Hero -->
<div class="hero-photo" role="img" aria-label="Smiling woman resting her chin on her hands beside a large model tooth, blue tinted"></div>
<svg class="abs" style="left:0;top:97px" width="1200" height="637" viewBox="0 0 1200 637">
  <path d="M0,395 C60,560 300,630 620,615 C860,600 1040,480 1200,300 L1200,330 C1040,500 860,618 620,630 C300,645 70,585 0,445 Z" fill="#69b12e"/>
  <path d="M0,445 C70,585 300,645 620,630 C860,618 1040,500 1200,330 L1200,637 L0,637 Z" fill="#ffffff"/>
</svg>
<h1 class="hero-title">Creating<br>Healthier Smiles</h1>
<p class="hero-sub">With Advanced Technology and Affordable Treatment</p>
<a class="btn btn-green" style="left:60px;top:409px;width:225px;height:40px">Book An Appointment</a>
<div class="social-dot" style="left:1106px;top:192px"></div>
<div class="social-dot" style="left:1106px;top:231px"></div>
<div class="social-dot" style="left:1106px;top:271px"></div>
<div class="social-dot" style="left:1106px;top:310px"></div>
<div class="abs" style="left:960px;top:605px;width:86px;height:1.5px;background:var(--blue)"></div>
<div class="slider-btn" style="left:1054px;top:586px;border:2px solid var(--green)">
  <svg width="14" height="14" viewBox="0 0 14 14"><path d="M9 2 4 7l5 5" fill="none" stroke="#69b12e" stroke-width="1.6"/></svg>
</div>
<div class="slider-btn" style="left:1100px;top:586px;border:1.5px solid var(--blue)">
  <svg width="14" height="14" viewBox="0 0 14 14"><path d="M5 2l5 5-5 5" fill="none" stroke="#2d9be6" stroke-width="1.6"/></svg>
</div>

<!-- Experience -->
<h2 class="section-title" style="top:766px;font-size:35px;line-height:41px">Experience the Halvern<br>Dental Difference</h2>
<div class="rule" style="left:571px;top:858px;width:57px"></div>
<div class="abs" style="left:165px;top:946px;width:60px;height:238px;background:var(--green)"></div>
<div class="abs" role="img" aria-label="Smiling dentist in a blue shirt seated beside a dental chair" style="left:193px;top:900px;width:338px;height:338px;background:linear-gradient(160deg,#f2f4f6 0%,#dfe6ec 55%,#b9cde0 100%)"></div>
<div class="about-text">
  <p>Your smile is our #1 priority. At Halvern Dental, we provide affordable and expert dental solutions. Whether you are looking for a family dentist or have any emergency such as needing a root canal in Westbrook, we are here for you! We want to keep your teeth healthy inside and out. We don't just clean teeth and send you on your way, we want to get to know you.</p>
  <p>We accept most HMO and PPO insurances. We offer various financing options through CarePay, Lendwise and In-House Plans.</p>
  <p>To constantly strive to achieve the highest level of skills and modern techniques and equipment so we can provide our patients with the best that Dentistry has to offer at our dental office in Westbrook, Westbrook County, CA.</p>
  <p>We provide patients with the best experience you can find in all of Southern California. We provide a comfortable and friendly atmosphere to shatter any fears you may have. We supply you with all the information on your dental health options so you can feel comfortable in the choices you make, whether it's a routine check-up or dental implants in Westbrook.</p>
</div>
<a class="about-link">We are available for Emergency and Walk-ins.</a>

<!-- Team -->
<div class="team-bg"></div>
<h2 class="section-title" style="top:1408px;font-size:34px">Meet Our Team</h2>
<p class="team-intro">Our Goal to serve you with the best service that we can offer. Our Exceptional team is always ready to give out Valuable Information so you may choose the right solution for your needs and condition.</p>
<div class="team-card" style="left:181px">
  <div class="team-photo" role="img" aria-label="Portrait of Dr. Nisha Varen"></div>
  <div class="team-name">Meet Dr. Nisha Varen</div><div class="team-role">Cosmetic Dentist</div>
</div>
<div class="team-card" style="left:469px">
  <div class="team-photo" role="img" aria-label="Portrait of Dr. Leela Marath"></div>
  <div class="team-name">Meet Dr. Leela Marath</div><div class="team-role">Endodontist</div>
</div>
<div class="team-card" style="left:758px">
  <div class="team-photo" role="img" aria-label="Portrait of Dr. Arun Kessel"></div>
  <div class="team-name">Meet Dr. Arun Kessel</div><div class="team-role">General Dentist</div>
</div>

<!-- Services -->
<svg class="abs" style="left:0;top:1878px" width="1200" height="650" viewBox="0 0 1200 650" role="img" aria-label="Dark tinted photo of a patient during a dental exam">
  <defs>
    <linearGradient id="nightFill" x1="0" y1="0" x2="1" y2="1">
      <stop offset="0" stop-color="#1a2d35"/><stop offset="0.6" stop-color="#14232a"/><stop offset="1" stop-color="#22343b"/>
    </linearGradient>
  </defs>
  <path d="M0,270 C0,150 300,55 640,70 C860,80 1050,300 1200,420 L1200,650 L0,650 Z" fill="url(#nightFill)"/>
  <path d="M0,270 C0,150 300,55 640,70 C860,80 1050,300 1200,420" fill="none" stroke="#69b12e" stroke-width="7"/>
</svg>
<div class="abs" role="img" aria-label="Woman smiling at a dentist holding a dental mirror" style="left:809px;top:1914px;width:284px;height:284px;border-radius:50%;border:7px solid var(--blue);background:linear-gradient(140deg,#e9d7c4 0%,#d8e6ef 60%,#b9d8ee 100%)"></div>
<h2 class="services-title">Our Services</h2>
<div class="rule" style="left:111px;top:2104px;width:55px"></div>
<p class="services-intro">We Value our Client's Smile. We know how Important it is for you to Have your Confidence Back.</p>

<svg width="0" height="0" style="position:absolute">
  <symbol id="tooth" viewBox="0 0 24 24"><path d="M7 3C4.5 3 3 5 3 7.5c0 2 1 3 1.5 5 .5 2.5.8 8 2.5 8 1.6 0 1.5-5 3-5h4c1.5 0 1.4 5 3 5 1.7 0 2-5.5 2.5-8 .5-2 1.5-3 1.5-5C21 5 19.5 3 17 3c-2 0-3 1-5 1S9 3 7 3z" fill="none" stroke="currentColor" stroke-width="1.3" stroke-linejoin="round"/></symbol>
</svg>

<div class="service" style="left:100px;top:2219px"><div class="service-icon is-active"><svg width="38" height="38" style="color:#fff"><use href="#tooth"/></svg></div><div class="service-label">Dental Implants</div></div>
<div class="service" style="left:265px;top:2219px"><div class="service-icon"><svg width="38" height="38" style="color:#69b12e"><use href="#tooth"/></svg></div><div class="service-label">Cosmetic Dentistry</div></div>
<div class="service" style="left:427px;top:2219px"><div class="service-icon"><svg width="38" height="38" style="color:#69b12e"><use href="#tooth"/></svg></div><div class="service-label">Braces</div></div>
<div class="service" style="left:590px;top:2219px"><div class="service-icon"><svg width="38" height="38" style="color:#69b12e"><use href="#tooth"/></svg></div><div class="service-label">Crowns</div></div>
<div class="service" style="left:750px;top:2219px"><div class="service-icon"><svg width="38" height="38" style="color:#69b12e"><use href="#tooth"/></svg></div><div class="service-label">Bridge</div></div>
<div class="service" style="left:915px;top:2219px"><div class="service-icon"><svg width="38" height="38" style="color:#69b12e"><use href="#tooth"/></svg></div><div class="service-label">Extractions</div></div>

<div class="service" style="left:100px;top:2354px"><div class="service-icon"><svg width="38" height="38" style="color:#69b12e"><use href="#tooth"/></svg></div><div class="service-label">Gum Disease</div></div>
<div class="service" style="left:265px;top:2354px"><div class="service-icon"><svg width="38" height="38" style="color:#69b12e"><use href="#tooth"/></svg></div><div class="service-label">Root Canal</div></div>
<div class="service" style="left:427px;top:2354px"><div class="service-icon"><svg width="38" height="38" style="color:#69b12e"><use href="#tooth"/></svg></div><div class="service-label">Dentures</div></div>
<div class="service" style="left:590px;top:2354px"><div class="service-icon"><svg width="38" height="38" style="color:#69b12e"><use href="#tooth"/></svg></div><div class="service-label">Emergency Dentistry</div></div>
<div class="service" style="left:750px;top:2354px"><div class="service-icon"><svg width="38" height="38" style="color:#69b12e"><use href="#tooth"/></svg></div><div class="service-label">Veneers</div></div>
<div class="service" style="left:915px;top:2354px"><div class="service-icon"><svg width="38" height="38" style="color:#69b12e"><use href="#tooth"/></svg></div><div class="service-label">ClearAlign Aligners</div></div>

<!-- Insurance band -->
<section class="insurance">
  <h3>No Insurance</h3>
  <p>Check Out Our CarePay Program.</p>
  <a class="btn btn-blue" style="left:605px;top:43px;width:224px;height:38px">View Our Programs</a>
  <svg class="abs" style="left:851px;top:41px" width="42" height="42" viewBox="0 0 42 42">
    <circle cx="21" cy="21" r="19" fill="none" stroke="#fff" stroke-width="2"/>
    <path d="M15 12c1-1 2 0 3 2s1 2 0 3l-1 1c1 2 3 4 5 5l1-1c1-1 1-1 3 0s3 2 2 3l-2 2c-6 0-12-6-12-12z" fill="#fff"/>
  </svg>
  <div class="abs" style="left:907px;top:42px;font-size:12px;color:#fff">Westbrook:</div>
  <div class="abs" style="left:907px;top:61px;font-size:17px;font-weight:600;color:#fff">(714) 555-0182</div>
</section>
<div class="abs" role="img" aria-label="White model tooth" style="left:166px;top:2512px;width:88px;height:151px;border-radius:40% 40% 30% 30%;background:linear-gradient(90deg,#c9ccce,#f6f6f6 50%,#bfc3c5)"></div>

<!-- Reviews -->
<h2 class="section-title" style="top:2722px;font-size:34px">What Our Patients Say About Us</h2>
<div class="rule" style="left:571px;top:2776px;width:57px"></div>
<div class="abs" style="left:0;top:2801px;width:1200px;text-align:center;font-size:13px">Average Rating</div>
<div class="abs" style="left:493px;top:2828px;font-size:32px;letter-spacing:3px;color:var(--star)">★★★★★</div>
<div class="abs" style="left:677px;top:2834px;font-size:18px;font-weight:700">4.9</div>
<svg class="abs" style="left:538px;top:2878px" width="30" height="26" viewBox="0 0 30 26"><circle cx="14" cy="12" r="11" fill="#2d9be6"/><circle cx="9" cy="12" r="1.6" fill="#fff"/><circle cx="14" cy="12" r="1.6" fill="#fff"/><circle cx="19" cy="12" r="1.6" fill="#fff"/></svg>
<div class="abs" style="left:578px;top:2882px;font-size:13px">238 Reviews</div>
<div class="arrow" style="left:198px;top:3040px">‹</div>
<div class="arrow" style="left:981px;top:3040px">›</div>
<div class="review-card">
  <div class="abs" role="img" aria-label="Reviewer avatar" style="left:31px;top:30px;width:82px;height:82px;border-radius:50%;background:radial-gradient(circle,#5a5652,#1c1b1a)"></div>
  <div class="abs" style="left:140px;top:30px;font-size:17px;letter-spacing:2px;color:var(--star)">★★★★★</div>
  <p class="review-text">Went here last July 2021 for the removal of my 1 impacted wisdom tooth. Office is clean, staff are courteous. Massage chair. Wait was quick. I chose the laughing gas and local anesthesia. Procedure is done in about 1 hour or less. Thumbs up to Dr Haldane and his assistance for the successful removal of my annoying molar. I recommend this office.</p>
  <div class="review-name">– &nbsp;Dorian K.</div>
  <div class="review-source">Revuo</div>
</div>

<!-- Promo -->
<div class="promo-photo" role="img" aria-label="Blue tinted dental office background"></div>
<div class="promo-person" role="img" aria-label="Smiling woman holding up a dental X-ray"></div>
<h2 class="promo-title">Committed to excellence in<br>Oral Health Care</h2>
<div class="rule" style="left:640px;top:3470px;width:55px;background:var(--green)"></div>
<p class="promo-sub">Free Exam and X-Rays for New Patients</p>
<a class="btn btn-green" style="left:637px;top:3517px;width:225px;height:40px">Book An Appointment</a>

<!-- Footer -->
<svg class="abs" style="left:0;top:3560px" width="1200" height="474" viewBox="0 0 1200 474">
  <path d="M0,190 C350,140 800,170 1200,55 L1200,474 L0,474 Z" fill="#15242b"/>
  <path d="M0,190 C350,140 800,170 1200,55" fill="none" stroke="#69b12e" stroke-width="8"/>
</svg>
<div class="footer-brand">Halvern Dental</div>
<a class="btn btn-green" style="left:59px;top:3948px;width:233px;height:37px;font-size:15px">Book Your Free Appointment</a>

<div class="footer-head" style="left:336px">Contact Us</div>
<svg class="abs" style="left:334px;top:3826px" width="18" height="22" viewBox="0 0 18 22"><path d="M9 1a7 7 0 0 0-7 7c0 5 7 13 7 13s7-8 7-13a7 7 0 0 0-7-7z" fill="none" stroke="#69b12e" stroke-width="2"/><circle cx="9" cy="8" r="2.5" fill="#69b12e"/></svg>
<div class="footer-line" style="left:369px;top:3824px">482 Orchard Vale Ave., Suite B<br>Westbrook, CA 92840</div>
<svg class="abs" style="left:334px;top:3879px" width="18" height="18" viewBox="0 0 18 18"><path d="M3 2c1-1 2 0 3 2s1 2 0 3l-1 1c1 2 3 4 5 5l1-1c1-1 1-1 3 0s3 2 2 3l-2 2C8 17 1 10 3 2z" fill="#69b12e"/></svg>
<div class="footer-line" style="left:369px;top:3878px;font-size:13px">(714) 555-0182</div>
<svg class="abs" style="left:334px;top:3914px" width="18" height="14" viewBox="0 0 18 14"><rect x="1" y="1" width="16" height="12" rx="1" fill="#69b12e"/><path d="M1 2l8 6 8-6" fill="none" stroke="#15242b" stroke-width="1.4"/></svg>
<div class="footer-line" style="left:369px;top:3911px">hello@halverndental.com</div>
<div class="social-dot" style="left:337px;top:3951px;width:30px;height:30px;border-color:var(--green)"></div>
<div class="social-dot" style="left:375px;top:3951px;width:30px;height:30px;border-color:var(--green)"></div>
<div class="social-dot" style="left:415px;top:3951px;width:30px;height:30px;border-color:var(--green)"></div>
<div class="social-dot" style="left:454px;top:3951px;width:30px;height:30px;border-color:var(--green)"></div>

<div class="footer-head" style="left:612px">Office Hours</div>
<svg class="abs" style="left:612px;top:3826px" width="18" height="18" viewBox="0 0 18 18"><circle cx="9" cy="9" r="7.5" fill="none" stroke="#69b12e" stroke-width="2"/><path d="M7 5.5v7l5.5-3.5z" fill="#69b12e"/></svg>
<div class="footer-line" style="left:643px;top:3824px;line-height:26.3px">Monday 10AM–7PM<br>Tuesday 10AM–7PM<br>Wednesday 9AM–6PM<br>Thursday 9AM–6PM<br>Friday 9AM–5PM<br>Saturday 9AM–1PM</div>

<div class="footer-head" style="left:886px">Location Map</div>
<div class="map" role="img" aria-label="Street map showing the Halvern Dental office location"></div>
<div class="footer-line" style="left:886px;top:3955px;width:290px;font-size:10.5px;line-height:21px">Crestline Dental | Elmwood Dental | Baywater Dental<br>| Tallis Dental | Portside Dental</div>

<div class="copyright">©Halvern Dental - 2021 All rights reserved. &nbsp;| Disclaimer &amp; Terms | Privacy Policy | Sitemap</div>

</body>
</html>
```